Technology Enablement - One Pager

I need (2) one pager piece of marketing collateral to use as outreach for a service offering. The one pager must have a strong call to action, highlight the pain points the service solves.

```html
<!DOCTYPE html>
<html lang="en">
<head>
<meta charset="utf-8">
<title>Trades Technology Enablement – One Pager</title>
<link href="https://fonts.googleapis.com/css2?family=Open+Sans:wght@400;600;700;800&family=Montserrat:wght@500;700;800&display=swap" rel="stylesheet">
<style>
  :root{
    --navy:#04305c;
    --yellow:#fdd15a;
    --gold:#fbd24c;
    --white:#ffffff;
    --ink:#111418;
    --paper-grey:#dcdcdc;
    --backdrop:#ececec;
  }
  *{box-sizing:border-box;margin:0;padding:0}
  html,body{width:1200px;height:1200px;overflow:hidden}
  body{background:var(--backdrop);font-family:"Open Sans",sans-serif;color:var(--ink)}
  .sheet{position:absolute;left:176px;top:0;width:848px;height:1200px;background:var(--white);overflow:hidden}
  .block{position:absolute;left:0;width:100%}
  ul{list-style:none}
  li{display:flex;align-items:center;gap:4px}
  li svg{flex:none}

  .masthead{top:0;height:83px;text-align:center;padding-top:24px}
  .masthead h1{font-weight:700;font-size:19.5px;color:var(--navy);line-height:1.2}
  .masthead p{font-size:17px;line-height:1.3;color:var(--ink)}

  .banner{top:83px;height:46px;background:var(--navy);display:flex;align-items:center;justify-content:center}
  .banner h2{font-weight:800;font-size:25px;color:var(--gold);letter-spacing:-.2px}

  .tagline{top:131px;text-align:center;font-size:23px;line-height:25px;color:var(--ink)}

  .reality{top:199px;height:239px;background:var(--navy);color:var(--white)}
  .reality .copy{position:absolute;left:23px;top:6px;width:360px;font-size:11px;line-height:14px}
  .reality h3{font-weight:700;font-size:18px;color:var(--gold);margin-bottom:5px}
  .reality .label{color:var(--gold);margin:7px 0 3px}
  .reality li{line-height:15.8px}
  .reality .closing{margin-top:6px}
  .reality .photo{position:absolute;left:430px;top:0;width:418px;height:239px;
    background:linear-gradient(90deg,rgba(4,48,92,1) 0%,rgba(4,48,92,0) 28%),
               linear-gradient(160deg,#5f86b8 0%,#2d5f99 45%,#1c3050 75%,#0f1c2c 100%)}

  .panel{position:absolute;height:183px;top:445px;padding:12px 23px 0 23px;font-size:11px;line-height:14px}
  .panel.what{left:0;width:420px;background:var(--yellow)}
  .panel.why{left:426px;width:422px;background:var(--navy);color:var(--white);padding-left:122px;padding-right:12px}
  .panel h3{font-weight:700;font-size:17.5px;margin-bottom:3px;line-height:1.2}
  .panel.why h3{color:var(--gold)}
  .panel p{margin-bottom:4px}
  .panel li{line-height:15.8px}
  .panel .closing{margin-top:6px}

  .product{top:645px;text-align:center}
  .product h2{font-weight:700;font-size:25px;line-height:31px;color:var(--navy)}
  .product p{font-size:11px;margin-top:18px}

  .detail{position:absolute;top:754px;height:165px;font-size:11px;line-height:15.8px;padding:14px 30px 0}
  .detail.review{left:0;width:420px;background:var(--navy);color:var(--white);padding-left:23px}
  .detail.receive{left:426px;width:422px;background:var(--yellow)}
  .detail h3{font-weight:700;font-size:17.5px;line-height:1.2;margin-bottom:2px}
  .detail.review h3{color:var(--gold)}
  .detail.receive h3{color:var(--navy)}
  .detail .lead{margin-bottom:5px}
  .detail .price{margin-top:6px;line-height:14px}
  .gap{display:inline-block;width:14px}

  .closer{top:927px;height:273px;background:linear-gradient(180deg,#e2e2e2,#d6d6d6);font-size:11px;line-height:15.8px}
  .closer .col{position:absolute;top:14px}
  .closer .who{left:23px;width:380px}
  .closer .why-start{left:456px;width:380px}
  .closer h3{font-weight:700;font-size:17.5px;line-height:1.2;color:var(--navy);margin-bottom:3px}
  .closer .lead{line-height:14px;margin-bottom:4px}
  .closer .sign-off{position:absolute;top:147px;left:0;width:100%;text-align:center;font-family:"Montserrat",sans-serif;font-weight:500;font-size:16.5px;color:var(--ink)}
  .cta{position:absolute;left:96px;top:185px;width:656px;height:47px;border-radius:14px;background:var(--navy);
    display:flex;align-items:center;justify-content:center;font-family:"Montserrat",sans-serif;font-weight:700;font-size:20.5px;color:var(--gold);text-decoration:none;letter-spacing:-.2px}
</style>
</head>
<body>
<svg width="0" height="0" style="position:absolute" aria-hidden="true">
  <symbol id="icon-box-check" viewBox="0 0 12 12"><rect x="1" y="1" width="10" height="10" fill="none" stroke="#fdd15a" stroke-width="1.2"/><path d="M3.2 6.2l2 2 3.8-4.4" fill="none" stroke="#fdd15a" stroke-width="1.3"/></symbol>
  <symbol id="icon-circle-check" viewBox="0 0 12 12"><circle cx="6" cy="6" r="4.8" fill="none" stroke="currentColor" stroke-width="1"/><path d="M3.6 6.2l1.7 1.7 3.1-3.4" fill="none" stroke="currentColor" stroke-width="1.1"/></symbol>
  <symbol id="icon-tick" viewBox="0 0 12 12"><path d="M2 6.4l2.8 2.8L10.4 3" fill="none" stroke="currentColor" stroke-width="1.3"/></symbol>
  <symbol id="icon-filled-check" viewBox="0 0 12 12"><rect x="1" y="1" width="10" height="10" rx="1" fill="#04305c"/><path d="M3.2 6.2l2 2 3.8-4.4" fill="none" stroke="#fff" stroke-width="1.3"/></symbol>
</svg>

<main class="sheet">
  <header class="block masthead">
    <h1>TECHNOLOGY ENABLEMENT FOR TRADES</h1>
    <p>(Electrical, Plumbing, HVAC, Mechanical, Construction)</p>
  </header>

  <div class="block banner"><h2>YOUR JOBS ARE PHYSICAL. YOUR PROBLEMS AREN’T.</h2></div>

  <p class="block tagline">We help trade businesses fix the tech<br>and workflows behind the work.</p>

  <section class="block reality">
    <div class="copy">
      <h3>The Reality in the Trades</h3>
      <p>Trade companies rely on technology more than ever —<br>even if they don’t call it “IT.”<br>Scheduling. Estimating. Job tracking. Invoicing. Payroll. Field apps.<br>Most of it works… kind of.</p>
      <p class="label">Common frustrations:</p>
      <ul>
        <li><svg width="11" height="11"><use href="#icon-box-check"/></svg>Office and field systems don’t line up</li>
        <li><svg width="11" height="11"><use href="#icon-box-check"/></svg>Dispatch process is manual or inefficient.</li>
        <li><svg width="11" height="11"><use href="#icon-box-check"/></svg>Jobs get quoted one way and invoiced another</li>
        <li><svg width="11" height="11"><use href="#icon-box-check"/></svg>Information is stuck in texts, notebooks, or someone’s phone</li>
        <li><svg width="11" height="11"><use href="#icon-box-check"/></svg>Admin work grows faster than revenue</li>
        <li><svg width="11" height="11"><use href="#icon-box-check"/></svg>Technology decisions fall to “whoever knows computers”</li>
      </ul>
      <p class="closing">The work gets done — but it takes more effort than it should.</p>
    </div>
    <div class="photo" role="img" aria-label="Photo of a consultant showing a technician in a hard hat a workflow on a monitor in an industrial workshop"></div>
  </section>

  <section class="panel what">
    <h3>What We Do</h3>
    <p>We help trade companies simplify operations using technology they already depend on.</p>
    <p>Northvale focuses on:</p>
    <ul>
      <li><svg width="10" height="10"><use href="#icon-circle-check"/></svg>How work flows from quote → job → invoice → reporting</li>
      <li><svg width="10" height="10"><use href="#icon-circle-check"/></svg>How office and field tools connect (or don’t)</li>
      <li><svg width="10" height="10"><use href="#icon-circle-check"/></svg>Where manual steps create delays, rework, or missed revenue</li>
      <li><svg width="10" height="10"><use href="#icon-circle-check"/></svg>Why tools aren’t being fully used by crews or admin staff</li>
    </ul>
    <p class="closing">This is about making the business easier to run — not selling IT jargon.</p>
  </section>

  <section class="panel why">
    <h3>Why Trades Like Our Approach</h3>
    <ul style="color:var(--white)">
      <li><svg width="10" height="10" style="color:var(--gold)"><use href="#icon-circle-check"/></svg>Low-risk, practical, and clear</li>
      <li><svg width="10" height="10" style="color:var(--gold)"><use href="#icon-circle-check"/></svg>No pressure to replace systems</li>
      <li><svg width="10" height="10" style="color:var(--gold)"><use href="#icon-circle-check"/></svg>No requirement to change IT providers</li>
      <li><svg width="10" height="10" style="color:var(--gold)"><use href="#icon-circle-check"/></svg>Focused on productivity, not tech for tech’s sake</li>
    </ul>
    <p class="closing">We earn trust by fixing real problems first.</p>
  </section>

  <section class="block product">
    <h2>PRODUCT 1: TRADES TECHNOLOGY<br>ENABLEMENT ASSESSMENT</h2>
    <p>A 2–4 week, stand-alone assessment built specifically for trades</p>
  </section>

  <section class="detail review">
    <h3>We review:</h3>
    <ul>
      <li><svg width="11" height="11"><use href="#icon-tick"/></svg>Job management workflows</li>
      <li><svg width="11" height="11"><use href="#icon-tick"/></svg>Quoting<span class="gap"></span>scheduling<span class="gap"></span>invoicing flow</li>
      <li><svg width="11" height="11"><use href="#icon-tick"/></svg>Field tools and adoption gaps</li>
      <li><svg width="11" height="11"><use href="#icon-tick"/></svg>Office vs field handoffs</li>
      <li><svg width="11" height="11"><use href="#icon-tick"/></svg>Reporting visibility (jobs, labour, margins)</li>
      <li><svg width="11" height="11"><use href="#icon-tick"/></svg>Security and data risks (without fear tactics)</li>
    </ul>
  </section>

  <section class="detail receive">
    <h3>You receive:</h3>
    <p class="lead">A Trades-Specific Improvement Roadmap showing:</p>
    <ul style="line-height:13.5px">
      <li><svg width="11" height="11"><use href="#icon-tick"/></svg>Where time and money are being lost</li>
      <li><svg width="11" height="11"><use href="#icon-tick"/></svg>What to fix first</li>
      <li><svg width="11" height="11"><use href="#icon-tick"/></svg>What can wait</li>
      <li><svg width="11" height="11"><use href="#icon-tick"/></svg>Where automation or integration actually pays off</li>
    </ul>
    <p class="price">Price: <strong>$2,500</strong><br>Straightforward. No obligation beyond the assessment.</p>
  </section>

  <section class="block closer">
    <div class="col who">
      <h3>Who This Is For</h3>
      <ul>
        <li><svg width="11" height="11"><use href="#icon-filled-check"/></svg>Electrical, plumbing, HVAC, mechanical, GC, and construction firms</li>
        <li><svg width="11" height="11"><use href="#icon-filled-check"/></svg>Owners feeling buried in admin</li>
        <li><svg width="11" height="11"><use href="#icon-filled-check"/></svg>Companies growing past “winging it”</li>
        <li><svg width="11" height="11"><use href="#icon-filled-check"/></svg>Trades relying on multiple apps that don’t work well together</li>
      </ul>
    </div>
    <div class="col why-start">
      <h3>Why Start With an Assessment</h3>
      <p class="lead">Because guessing costs more than clarity.<br>This gives you:</p>
      <ul>
        <li><svg width="11" height="11"><use href="#icon-filled-check"/></svg>A clear plan instead of piecemeal fixes</li>
        <li><svg width="11" height="11"><use href="#icon-filled-check"/></svg>Confidence before spending on new tools</li>
        <li><svg width="11" height="11"><use href="#icon-filled-check"/></svg>A roadmap aligned to how trades actually work</li>
      </ul>
    </div>
    <p class="sign-off">Fix the systems behind the scenes — so the work runs smoother on site.</p>
    <a class="cta" href="#book">BOOK A TRADES TECHNOLOGY ENABLEMENT ASSESSMENT</a>
  </section>
</main>
</body>
</html>
```